Intermodal Trucking Company Website

My client is a trucking company that takes the containers you see on the back of a ship or railroad car and delivers them in the midwestern part of the United States. Here are some of their competitors Websites and their logo to use as part of the design.

http://www.varnekhaulers.example/
https://www.plirext.example/
http://www.brontagefreight.example/
https://www.lqp-xy.example/

Industry/Entity Type

Trucking Company

Number of Pages Required

2 page

Requirements
Must have
• Website must be professional and the design needs to be suitable for a responsive Website.
Should not have
• Please do not submit designs with misspellings. Designs with misspellings will be eliminated.

```html
<!DOCTYPE html>
<html lang="en">
<head>
<meta charset="utf-8">
<title>Tallgrass Haul Co</title>
<link href="https://fonts.googleapis.com/css2?family=Open+Sans:wght@400;600&display=swap" rel="stylesheet">
<style>
:root{
  --accent:#c0392b;
  --nav:#fff23a;
  --nav-text:#7a6a3a;
  --ink:#222;
  --muted:#666;
  --field:#ededed;
  --band:#f2f2f2;
  --footer:#3d3d3d;
  --footer-text:#bdbdbd;
  --dark-btn:#1f1f1f;
}
*{box-sizing:border-box;margin:0;padding:0}
html,body{width:958px;height:1200px;overflow:hidden}
body{font-family:"Open Sans",Arial,sans-serif;color:var(--ink);background:#fff;position:relative}
.hero{position:absolute;left:0;top:0;width:958px;height:490px;
  background:linear-gradient(180deg,#3e6a9a 0%,#9aa6bd 25%,#e8b893 45%,#c98a56 62%,#7b6a5e 75%,#5b5c66 100%)}
.hero-arrow{position:absolute;top:233px}
.hero-arrow.prev{left:20px}
.hero-arrow.next{left:915px}
.brand{position:absolute;left:106px;top:0;width:153px;height:160px;background:#fff;
  display:flex;flex-direction:column;align-items:center;justify-content:center;gap:8px;text-align:center;
  box-shadow:0 1px 3px rgba(0,0,0,.15)}
.brand-mark{width:22px;height:22px;background:var(--accent)}
.brand-name{font-weight:600;font-size:15px;line-height:1.2;color:var(--accent)}
.nav{position:absolute;left:258px;top:0;width:595px;height:32px;background:var(--nav);
  display:flex;justify-content:flex-end;align-items:center;gap:27px;padding-right:13px}
.nav a{font-size:10px;color:var(--nav-text);text-decoration:none;text-transform:uppercase}
.nav a.active{color:#111;font-weight:600;text-decoration:underline}
.intro{position:absolute;left:0;top:546px;width:958px;text-align:center}
.intro h1{font-size:25px;font-weight:400;color:var(--accent);letter-spacing:.5px}
.intro p{width:724px;margin:10px auto 0;font-size:11.5px;line-height:18px}
.btn-outline{display:inline-block;margin-top:15px;width:84px;height:33px;line-height:31px;border:1px solid #888;font-size:12px;color:var(--ink)}
.card{position:absolute;top:718px;width:238px}
.card-media{width:238px;height:153px}
.card h2{margin-top:8px;font-size:16px;font-weight:400;color:var(--accent)}
.card .date{font-size:7px;color:var(--muted);margin-top:6px}
.card p.small{font-size:7px;line-height:13px;color:var(--muted);margin-top:7px;height:52px}
.card p.lead{font-size:9px;line-height:14px;margin-top:5px;height:28px}
.btn-soft{position:absolute;top:248px;left:0;width:77px;height:29px;line-height:29px;background:var(--field);font-size:9px;color:#666;text-align:center}
.field{position:absolute;left:0;width:179px;height:38px;background:var(--field);font-size:9px;color:#777;padding-left:16px;line-height:38px}
.btn-dark{position:absolute;left:187px;top:239px;width:51px;height:38px;background:var(--dark-btn);color:#fff;font-size:9px;text-align:center;line-height:38px}
.contact-band{position:absolute;left:0;top:1059px;width:958px;height:64px;background:var(--band);
  display:flex;justify-content:space-between;align-items:center;padding:0 106px;font-size:10.5px;color:#333}
.contact-band span{display:flex;align-items:center;gap:6px}
.footer{position:absolute;left:0;top:1123px;width:958px;height:77px;background:var(--footer);color:var(--footer-text);font-size:8px}
.footer-links{position:absolute;left:106px;top:23px}
.footer-links a{color:var(--footer-text);text-decoration:none}
.footer-links i{font-style:normal;margin:0 7px}
.copyright{position:absolute;left:106px;top:44px}
.social{position:absolute;left:798px;top:27px;display:flex;gap:7px}
.social span{width:23px;height:23px;border-radius:50%;background:#8a8a8a;display:block}
</style>
</head>
<body>
<div class="hero" role="img" aria-label="Photo of a semi truck driving on a highway at sunset between golden hills"></div>
<svg class="hero-arrow prev" width="20" height="20" viewBox="0 0 20 20"><path d="M12 4 6 10l6 6" fill="none" stroke="#ddd" stroke-width="2.5"/></svg>
<svg class="hero-arrow next" width="23" height="23" viewBox="0 0 23 23"><circle cx="11.5" cy="11.5" r="11.5" fill="#888"/><path d="M9.5 6l5.5 5.5L9.5 17" fill="none" stroke="#eee" stroke-width="2.5"/></svg>

<div class="brand">
  <span class="brand-mark"></span>
  <span class="brand-name">Tallgrass<br>Haul Co<br>Kansas City, KS</span>
</div>

<nav class="nav">
  <a class="active" href="#">Home</a>
  <a href="#">About Us</a>
  <a href="#">Products</a>
  <a href="#">News</a>
  <a href="#">Contact Us</a>
</nav>

<section class="intro">
  <h1>TALLGRASS HAUL CO</h1>
  <p>Call us for all your intermodal container movement needs out of the Kansas City, KS or MO area. We have been in business for over 20 years handling all types of container movement including hazmat movements to anywhere within the 48 states.</p>
  <span class="btn-outline">Contact Us</span>
</section>

<article class="card" style="left:106px">
  <div class="card-media" role="img" aria-label="Photo of a red semi truck with a silver trailer under a blue sky" style="background:linear-gradient(180deg,#4f7fb5 0%,#b9cde0 60%,#55555a 100%)"></div>
  <h2>OUR TRUCKS</h2>
  <p class="small">Donec ac quam lorem. Sed et magna libero. Cras nibh tortor, tempor eu condimentum a, auctor eu risus. Cras et consectetur nibh, id finibus velit. Ut molestie nunc a turpis posuere pretium. Orci varius natoque penatibus et magnis.</p>
  <span class="btn-soft">Read more</span>
</article>

<article class="card" style="left:361px">
  <div class="card-media" role="img" aria-label="Photo of a white delivery van parked beside trucks at a depot" style="background:linear-gradient(180deg,#7fb3e6 0%,#d7dde4 45%,#a9a9a6 100%)"></div>
  <h2>NEWS</h2>
  <p class="date">1 April, 2017</p>
  <p class="lead">Integer cursus justo orci, lacinia ultrices nisi elementum vitae. Maecenas iaculis posuere nisi mattis.</p>
  <span class="btn-soft">Read more</span>
</article>

<article class="card" style="left:615px">
  <div class="card-media" role="img" aria-label="Photo of a driver holding a clipboard in front of a green truck" style="background:linear-gradient(135deg,#c9d3d8 0%,#7fbf7a 45%,#9a9c95 100%)"></div>
  <h2>TRACKING</h2>
  <span class="field" style="top:191px">Reference Bill Number</span>
  <span class="field" style="top:239px">Container</span>
  <span class="btn-dark">Track It</span>
</article>

<section class="contact-band">
  <span><svg width="8" height="8" viewBox="0 0 10 10"><path d="M2 0h2l1 2.5-1.3 1a6 6 0 0 0 2.8 2.8l1-1.3L10 6v2c0 1-1 2-2 2A8 8 0 0 1 0 2c0-1 1-2 2-2z" fill="#333"/></svg>Phone : 913-555-0147</span>
  <span><svg width="8" height="8" viewBox="0 0 10 10"><path d="M2 0h2l1 2.5-1.3 1a6 6 0 0 0 2.8 2.8l1-1.3L10 6v2c0 1-1 2-2 2A8 8 0 0 1 0 2c0-1 1-2 2-2z" fill="#333"/></svg>Toll Free : 800-555-0182</span>
  <span><svg width="8" height="8" viewBox="0 0 10 10"><rect x="0" y="3" width="10" height="7" fill="#333"/><rect x="2" y="0" width="6" height="4" fill="#333"/></svg>Fax : 913-555-0163</span>
  <span><svg width="9" height="7" viewBox="0 0 10 8"><rect width="10" height="8" fill="#333"/><path d="M0 0l5 4 5-4" fill="none" stroke="#f2f2f2"/></svg>Email : dispatch@tallgrasshaul.example</span>
</section>

<footer class="footer">
  <div class="footer-links"><a href="#">Home</a><i>|</i><a href="#">About Us</a><i>|</i><a href="#">Products</a><i>|</i><a href="#">News</a><i>|</i><a href="#">Contact Us</a></div>
  <div class="copyright">Copyright &copy; 2017 Company name. All rights reserved</div>
  <div class="social"><span></span><span></span></div>
</footer>
</body>
</html>
```